DILIGENCE COUNTS, OSRL, velmontsurety.net, New Infographic Design Project

Velmontsurety.net
Infographic
See attached information
Would like charts showing where funds from each bond goes

For design inspiration only, do not copy any of the elements - https://www.plorvexgallery.com/design/5820417

up coming Wardens summit! we would like something professional outlining our industries benefits to the justice process in Arkansas

see attached information. we would like similar graphics pie chart showing where money goes from each bond written etc.

Target Market(s)

Government law enforcement

Industry/Entity Type

Judicial

Requirements
Must have
• Professional graphics charts

```html
<!DOCTYPE html>
<html lang="en">
<head>
<meta charset="utf-8">
<title>OSRL – Today's Bail Bondsman</title>
<link href="https://fonts.googleapis.com/css2?family=Montserrat:wght@400;600;700;800&family=Arimo:wght@400;700&display=swap" rel="stylesheet">
<style>
  :root {
    --navy: #2b3c5c;
    --navy-deep: #1f2d48;
    --navy-soft: #4a5c7e;
    --red: #b8323c;
    --stage: #e7e8e9;
    --paper: #ffffff;
    --ink: #2a2a2a;
    --amount: #2e4068;
  }
  * { box-sizing: border-box; margin: 0; padding: 0; }
  html, body { width: 1200px; height: 1014px; overflow: hidden; }
  body { background: var(--stage); font-family: "Arimo", Arial, sans-serif; color: var(--ink); position: relative; }

  .flyer { position: absolute; left: 280px; top: 55px; width: 638px; height: 903px; background: var(--paper); overflow: hidden; }

  .masthead { position: absolute; left: 0; top: 0; width: 638px; height: 76px; background: var(--navy); }
  .brand { position: absolute; left: 0; right: 0; top: 24px; text-align: center; color: #fff; }
  .brand-name { font-family: "Montserrat", sans-serif; font-weight: 800; font-size: 22px; letter-spacing: 1px; display: inline-flex; align-items: center; gap: 7px; }
  .brand-mark { width: 14px; height: 14px; background: var(--red); display: inline-block; }
  .brand-tagline { font-family: "Montserrat", sans-serif; font-weight: 800; font-size: 6.5px; letter-spacing: .3px; margin-top: 1px; }

  .hero { position: absolute; left: 0; top: 76px; width: 638px; height: 252px; }
  .hero-photo { position: absolute; inset: 0; background:
      radial-gradient(ellipse at 70% 65%, rgba(214,150,60,.55), transparent 55%),
      radial-gradient(ellipse at 25% 80%, rgba(190,130,60,.4), transparent 50%),
      linear-gradient(180deg, #1c2a44 0%, #2a3550 45%, #4a3c30 100%); }
  .hero-edge { position: absolute; left: 0; top: 0; width: 638px; height: 40px; }
  .hero-title { position: absolute; left: 0; right: 0; top: 72px; text-align: center; color: #fff; font-family: "Montserrat", sans-serif; font-weight: 800; font-size: 29px; letter-spacing: .3px; }
  .hero-copy { position: absolute; left: 136px; width: 366px; top: 118px; text-align: center; color: #fff; font-size: 13.4px; line-height: 16.8px; }

  .stats { position: absolute; left: 0; top: 328px; width: 638px; height: 211px; }
  .stat { position: absolute; top: 0; height: 211px; width: 200px; margin-left: -100px; text-align: center; font-size: 13.4px; line-height: 16.5px; color: var(--ink); }
  .stat-wide { width: 230px; margin-left: -115px; }
  .stat-lead { position: absolute; left: 0; right: 0; bottom: 153px; }
  .stat-dial { position: absolute; left: 62px; top: 63px; width: 76px; height: 76px; border-radius: 50%;
      background: radial-gradient(circle at 70% 25%, #7d8ba6 0%, var(--navy-soft) 30%, var(--navy-deep) 100%);
      color: #fff; font-family: "Montserrat", sans-serif; font-weight: 700; font-size: 19px; line-height: 76px; }
  .stat-wide .stat-dial { left: 77px; }
  .stat-foot { position: absolute; left: 0; right: 0; top: 146px; line-height: 17px; text-transform: uppercase; }
  .stat-foot.plain { text-transform: none; }

  .fees-banner { position: absolute; left: 0; top: 539px; width: 638px; height: 69px; }
  .fees-banner-text { position: absolute; left: 0; right: 0; top: 14px; text-align: center; color: #fff; font-family: "Montserrat", sans-serif; text-transform: uppercase; }
  .fees-banner-text .line-one { font-size: 13px; font-weight: 400; letter-spacing: .4px; }
  .fees-banner-text .line-two { font-size: 15.5px; font-weight: 700; margin-top: 3px; }

  .fee { position: absolute; font-size: 13.4px; line-height: 16px; color: var(--ink); }
  .fee-amount { position: relative; color: var(--amount); font-family: "Montserrat", sans-serif; font-weight: 700; font-size: 16px; line-height: 21px; }
  .fee-amount small { font-family: "Arimo", sans-serif; font-weight: 400; font-size: 14px; }
  .fee-amount::before { content: ""; position: absolute; left: -20px; top: 4px; border-left: 13px solid var(--red); border-top: 7px solid transparent; border-bottom: 7px solid transparent; }
  .fee-total .fee-amount { font-size: 24px; line-height: 30px; }
  .fee-total .fee-amount::before { top: 8px; }
  .col-left { left: 83px; width: 210px; }
  .col-right { left: 393px; width: 220px; }
</style>
</head>
<body>
<article class="flyer">
  <header class="masthead">
    <div class="brand">
      <div class="brand-name"><span class="brand-mark"></span>OSRL</div>
      <div class="brand-tagline">ozark surety responders league</div>
    </div>
  </header>

  <section class="hero">
    <div class="hero-photo" role="img" aria-label="Night aerial view of a city with lit streets and a courthouse"></div>
    <svg class="hero-edge" viewBox="0 0 638 40" preserveAspectRatio="none">
      <polygon points="0,0 638,0 638,12 0,0" fill="#2b3c5c"/>
      <polygon points="0,0 638,12 638,26 300,16 0,14" fill="rgba(255,255,255,.55)"/>
      <polygon points="0,0 300,16 0,26" fill="#b8323c"/>
    </svg>
    <h1 class="hero-title">TODAY’S BAIL BONDSMAN</h1>
    <p class="hero-copy">Arkansas is one of the only states with a regulatory licensing board and an owner funded Association with a full-time lobbyist.&nbsp; We work with all law enforcement agencies to secure better legislation for Arkansas and the criminal justice system.</p>
  </section>

  <section class="stats">
    <div class="stat" style="left:102px">
      <div class="stat-lead">Our industry<br>maintains a</div>
      <div class="stat-dial">2.4%</div>
      <div class="stat-foot">Failure to<br>appear rate</div>
    </div>
    <div class="stat" style="left:303px">
      <div class="stat-lead">All other forms of pre-trial<br>release average a</div>
      <div class="stat-dial">40%</div>
      <div class="stat-foot">Failure to<br>appear rate</div>
    </div>
    <div class="stat stat-wide" style="left:504px">
      <div class="stat-lead">We are</div>
      <div class="stat-dial">100%</div>
      <div class="stat-foot plain">responsible for extradition<br>fees on our clients with no<br>cost to the taxpayer</div>
    </div>
  </section>

  <section class="fees-banner">
    <svg width="638" height="69" viewBox="0 0 638 69">
      <polygon points="0,0 36,0 0,55" fill="#b8323c"/>
      <polygon points="638,0 602,0 638,55" fill="#b8323c"/>
      <polygon points="36,0 602,0 567,69 71,69" fill="#2b3c5c"/>
    </svg>
    <div class="fees-banner-text">
      <div class="line-one">Legislativity&nbsp; mandated fees collected for</div>
      <div class="line-two">Every bond executed by the bondsman</div>
    </div>
  </section>

  <div class="fee col-left" style="top:637px">
    <div>Arkansas Wardens’ Council</div>
    <div class="fee-amount">$6.00 <small>Per Bond</small></div>
    <div>100% Of The Budget</div>
  </div>
  <div class="fee col-left" style="top:703px">
    <div>Arkansas Public Counsel<br>Commission</div>
    <div class="fee-amount">$20.00 <small>Per Bond</small></div>
    <div>2/3 Of Their Budget</div>
  </div>
  <div class="fee col-left" style="top:786px">
    <div>Arkansas Family<br>Safety &amp; Violence<br>Commission</div>
    <div class="fee-amount">$4.00 <small>Per Bond</small></div>
  </div>

  <div class="fee col-right" style="top:637px">
    <div>Bail Bond Recovery Fund (Paid<br>To The County General Fund)</div>
    <div class="fee-amount">$4.00 <small>Per Bond</small></div>
  </div>
  <div class="fee col-right" style="top:719px">
    <div>State General Revenue And<br>Agency Operation</div>
    <div class="fee-amount">$6.00 <small>Per Bond</small></div>
  </div>
  <div class="fee col-right fee-total" style="top:797px">
    <div>Total Revenue Generated<br>In 2019 Pre-covid</div>
    <div class="fee-amount" style="margin-top:4px">$3,476,160.00</div>
  </div>
</article>
</body>
</html>
```